Newspaper advert design

Chinese Horoscopes : Needed the 12 animals one for males, one for females. Listed against the name and picture of animal, the telephone number of a premium rate telephone line.. So in total 24 phone numbers.

Two columns for a half a page newspaper/magazine advertisement. 12 zodiac signs for females - 12 zodiac signs for males.

Eye catching colors needed. Bright colors.

The Chinese animals symbols to look as "cartoon-ish as possible) Bold rounded fonts.

Chinese Horoscopes :  Needed the 12 animals one for males, one for females.  Listed against the name and picture of animal, the telephone number of a premium rate telephone line..  So in total 24 phone numbers.

Two columns for a half a page newspaper/magazine advertisement.  12 zodiac signs for females - 12 zodiac signs for males.

The Chinese animals symbols to look as "cartoon-ish as possible)  Bold rounded fonts.

Must have the slogan "Find your inner animal" underneath the list.

Target Market(s)

Women age rage 18 to 60.

Requirements
Must have
• Bright colors.
Bold fonts.

The heading Chinese Horoscopes

"Find your inner animal" at the bottom of the advertisement.

```html
<!DOCTYPE html>
<html lang="en">
<head>
<meta charset="utf-8">
<title>Chinese Horoscope</title>
<link rel="stylesheet" href="https://fonts.googleapis.com/css2?family=Cinzel:wght@600;700&family=PT+Serif:wght@700&display=swap">
<style>
  :root {
    --page-bg: #3a2b22;
    --red: #b3293f;
    --rose: #c8506a;
    --amber: #f2c95a;
    --glow: #fdf3a6;
    --teal: #1f8a8f;
    --deep-teal: #0d3d4c;
    --female-light: #8f2f6f;
    --female-dark: #3b0e2b;
    --male-light: #2f8f99;
    --male-dark: #0c2c3b;
    --gold: #d9b45a;
    --rate: #ffd93b;
    --ink-light: #ffffff;
    --label: #f6e8d0;
  }
  * { box-sizing: border-box; margin: 0; padding: 0; }
  html, body { width: 1200px; height: 960px; overflow: hidden; }
  body { background: var(--page-bg); position: relative; font-family: "PT Serif", Georgia, serif; }

  .poster {
    position: absolute; left: 275px; top: 20px; width: 650px; height: 920px; overflow: hidden;
    background:
      radial-gradient(ellipse 38% 48% at 50% 52%, var(--glow) 0%, rgba(253,243,166,0) 100%),
      linear-gradient(90deg, var(--red) 0%, var(--rose) 14%, var(--amber) 38%, var(--amber) 60%, var(--teal) 86%, var(--deep-teal) 100%);
    box-shadow: 0 6px 24px rgba(0,0,0,.5);
  }
  .poster-backdrop {
    position: absolute; inset: 60px 40px 0 40px;
    background: radial-gradient(ellipse 60% 70% at 50% 45%, rgba(120,40,40,.18), rgba(0,0,0,0));
  }

  .title {
    position: absolute; top: 30px; left: 0; right: 0; text-align: center;
    font-family: "Cinzel", "Times New Roman", serif; font-weight: 700; font-size: 33px;
    color: #fff7ea; letter-spacing: 1px; text-shadow: 0 2px 3px rgba(60,20,10,.6);
  }
  .dragon {
    position: absolute; top: 18px; width: 90px; height: 66px; border-radius: 40%;
    background: radial-gradient(circle at 45% 45%, #f1d38a, var(--gold) 55%, rgba(140,100,40,0) 75%);
  }
  .dragon-left { left: 12px; }
  .dragon-right { right: 12px; }

  .column-head {
    position: absolute; top: 100px; height: 40px; display: flex; align-items: center; justify-content: center; gap: 10px;
    border-radius: 6px; border: 1px dashed rgba(255,255,255,.55);
    font-family: "Cinzel", "Times New Roman", serif; font-weight: 700; font-size: 24px; color: #fff7ea;
  }
  .column-head-female { left: 100px; width: 204px; background: var(--female-dark); }
  .column-head-male { left: 346px; width: 204px; background: var(--male-dark); }
  .head-ornament { width: 22px; height: 14px; border-radius: 50%; background: var(--gold); opacity: .85; }

  .sign-list { position: absolute; top: 154px; width: 204px; height: 696px; }
  .sign-list-female { left: 100px; }
  .sign-list-male { left: 346px; }
  .sign { position: relative; height: 58px; }
  .sign-name {
    position: absolute; top: 0; font-family: "Cinzel", "Times New Roman", serif; font-weight: 600;
    font-size: 10px; line-height: 11px; color: var(--label); text-shadow: 0 1px 2px rgba(0,0,0,.5); width: 52px; text-align: center;
  }
  .sign-art {
    position: absolute; top: 12px; width: 50px; height: 43px; border: 2px solid #fff; border-radius: 3px;
    background: linear-gradient(135deg, #e8e4f8, #fbe2ea 55%, #f7d7a8);
    box-shadow: 0 1px 3px rgba(0,0,0,.4);
  }
  .rate-card {
    position: absolute; top: 18px; width: 148px; height: 32px; border-radius: 5px;
    padding: 3px 8px; outline: 1px dashed rgba(255,255,255,.45); outline-offset: -3px;
    font-size: 9.5px; line-height: 13px; white-space: nowrap;
  }
  .rate-card .rate { color: var(--rate); }
  .rate-card .phone { color: var(--ink-light); }

  .sign-list-female .sign-name, .sign-list-female .sign-art { left: 0; }
  .sign-list-female .rate-card { left: 54px; }
  .sign-list-male .rate-card { left: 0; }
  .sign-list-male .sign-name, .sign-list-male .sign-art { left: 152px; }

  .sign:nth-child(odd) .rate-card.female { background: var(--female-light); }
  .sign:nth-child(even) .rate-card.female { background: var(--female-dark); }
  .sign:nth-child(odd) .rate-card.male { background: var(--male-light); }
  .sign:nth-child(even) .rate-card.male { background: var(--male-dark); }

  .slogan {
    position: absolute; top: 864px; left: 0; right: 0; text-align: center;
    font-family: "Cinzel", "Times New Roman", serif; font-weight: 700; font-size: 24px;
    color: #fff7ea; letter-spacing: 1px; text-shadow: 0 2px 3px rgba(60,20,10,.6);
  }
</style>
</head>
<body>
<main class="poster">
  <div class="poster-backdrop" role="img" aria-label="Faint silhouettes of a woman and a man with swirling floral ornament"></div>

  <div class="dragon dragon-left" role="img" aria-label="Golden dragon ornament"></div>
  <h1 class="title">Chinese Horoscope</h1>
  <div class="dragon dragon-right" role="img" aria-label="Golden dragon ornament"></div>

  <div class="column-head column-head-female">
    <span class="head-ornament" role="img" aria-label="Small gold dragon"></span>Female<span class="head-ornament" role="img" aria-label="Small gold dragon"></span>
  </div>
  <div class="column-head column-head-male">
    <span class="head-ornament" role="img" aria-label="Small gold dragon"></span>Male<span class="head-ornament" role="img" aria-label="Small gold dragon"></span>
  </div>

  <section class="sign-list sign-list-female">
    <div class="sign"><span class="sign-name">Rat</span><div class="sign-art" role="img" aria-label="Cartoon girl in rat costume"></div><div class="rate-card female"><div class="rate">Premium Rate : 50 ¥</div><div class="phone">Telephone: 123-456-7890</div></div></div>
    <div class="sign"><span class="sign-name">Ox</span><div class="sign-art" role="img" aria-label="Cartoon girl in ox costume"></div><div class="rate-card female"><div class="rate">Premium Rate : 50 ¥</div><div class="phone">Telephone: 123-456-7890</div></div></div>
    <div class="sign"><span class="sign-name">Tiger</span><div class="sign-art" role="img" aria-label="Cartoon girl in tiger costume"></div><div class="rate-card female"><div class="rate">Premium Rate : 50 ¥</div><div class="phone">Telephone: 123-456-7890</div></div></div>
    <div class="sign"><span class="sign-name">Rabbit</span><div class="sign-art" role="img" aria-label="Cartoon girl in rabbit costume"></div><div class="rate-card female"><div class="rate">Premium Rate : 50 ¥</div><div class="phone">Telephone: 123-456-7890</div></div></div>
    <div class="sign"><span class="sign-name">Dragon</span><div class="sign-art" role="img" aria-label="Cartoon girl in dragon costume"></div><div class="rate-card female"><div class="rate">Premium Rate : 50 ¥</div><div class="phone">Telephone: 123-456-7890</div></div></div>
    <div class="sign"><span class="sign-name">Snake</span><div class="sign-art" role="img" aria-label="Cartoon girl in snake costume"></div><div class="rate-card female"><div class="rate">Premium Rate : 50 ¥</div><div class="phone">Telephone: 123-456-7890</div></div></div>
    <div class="sign"><span class="sign-name">Horse</span><div class="sign-art" role="img" aria-label="Cartoon girl in horse costume"></div><div class="rate-card female"><div class="rate">Premium Rate : 50 ¥</div><div class="phone">Telephone: 123-456-7890</div></div></div>
    <div class="sign"><span class="sign-name">Goat</span><div class="sign-art" role="img" aria-label="Cartoon girl in goat costume"></div><div class="rate-card female"><div class="rate">Premium Rate : 50 ¥</div><div class="phone">Telephone: 123-456-7890</div></div></div>
    <div class="sign"><span class="sign-name">Monkey</span><div class="sign-art" role="img" aria-label="Cartoon girl in monkey costume"></div><div class="rate-card female"><div class="rate">Premium Rate : 50 ¥</div><div class="phone">Telephone: 123-456-7890</div></div></div>
    <div class="sign"><span class="sign-name">Rooster</span><div class="sign-art" role="img" aria-label="Cartoon girl in rooster costume"></div><div class="rate-card female"><div class="rate">Premium Rate : 50 ¥</div><div class="phone">Telephone: 123-456-7890</div></div></div>
    <div class="sign"><span class="sign-name">Dog</span><div class="sign-art" role="img" aria-label="Cartoon girl in dog costume"></div><div class="rate-card female"><div class="rate">Premium Rate : 50 ¥</div><div class="phone">Telephone: 123-456-7890</div></div></div>
    <div class="sign"><span class="sign-name">Pig</span><div class="sign-art" role="img" aria-label="Cartoon girl in pig costume"></div><div class="rate-card female"><div class="rate">Premium Rate : 50 ¥</div><div class="phone">Telephone: 123-456-7890</div></div></div>
  </section>

  <section class="sign-list sign-list-male">
    <div class="sign"><div class="rate-card male"><div class="rate">Premium Rate : 50 ¥</div><div class="phone">Telephone: 123-456-7890</div></div><span class="sign-name">Rat</span><div class="sign-art" role="img" aria-label="Cartoon boy in rat costume"></div></div>
    <div class="sign"><div class="rate-card male"><div class="rate">Premium Rate : 50 ¥</div><div class="phone">Telephone: 123-456-7890</div></div><span class="sign-name">Ox</span><div class="sign-art" role="img" aria-label="Cartoon boy in ox costume"></div></div>
    <div class="sign"><div class="rate-card male"><div class="rate">Premium Rate : 50 ¥</div><div class="phone">Telephone: 123-456-7890</div></div><span class="sign-name">Tiger</span><div class="sign-art" role="img" aria-label="Cartoon boy in tiger costume"></div></div>
    <div class="sign"><div class="rate-card male"><div class="rate">Premium Rate : 50 ¥</div><div class="phone">Telephone: 123-456-7890</div></div><span class="sign-name">Rabbit</span><div class="sign-art" role="img" aria-label="Cartoon boy in rabbit costume"></div></div>
    <div class="sign"><div class="rate-card male"><div class="rate">Premium Rate : 50 ¥</div><div class="phone">Telephone: 123-456-7890</div></div><span class="sign-name">Dragon</span><div class="sign-art" role="img" aria-label="Cartoon boy in dragon costume"></div></div>
    <div class="sign"><div class="rate-card male"><div class="rate">Premium Rate : 50 ¥</div><div class="phone">Telephone: 123-456-7890</div></div><span class="sign-name">Snake</span><div class="sign-art" role="img" aria-label="Cartoon boy in snake costume"></div></div>
    <div class="sign"><div class="rate-card male"><div class="rate">Premium Rate : 50 ¥</div><div class="phone">Telephone: 123-456-7890</div></div><span class="sign-name">Horse</span><div class="sign-art" role="img" aria-label="Cartoon boy in horse costume"></div></div>
    <div class="sign"><div class="rate-card male"><div class="rate">Premium Rate : 50 ¥</div><div class="phone">Telephone: 123-456-7890</div></div><span class="sign-name">Goat</span><div class="sign-art" role="img" aria-label="Cartoon boy in goat costume"></div></div>
    <div class="sign"><div class="rate-card male"><div class="rate">Premium Rate : 50 ¥</div><div class="phone">Telephone: 123-456-7890</div></div><span class="sign-name">Monkey</span><div class="sign-art" role="img" aria-label="Cartoon boy in monkey costume"></div></div>
    <div class="sign"><div class="rate-card male"><div class="rate">Premium Rate : 50 ¥</div><div class="phone">Telephone: 123-456-7890</div></div><span class="sign-name">Rooster</span><div class="sign-art" role="img" aria-label="Cartoon boy in rooster costume"></div></div>
    <div class="sign"><div class="rate-card male"><div class="rate">Premium Rate : 50 ¥</div><div class="phone">Telephone: 123-456-7890</div></div><span class="sign-name">Dog</span><div class="sign-art" role="img" aria-label="Cartoon boy in dog costume"></div></div>
    <div class="sign"><div class="rate-card male"><div class="rate">Premium Rate : 50 ¥</div><div class="phone">Telephone: 123-456-7890</div></div><span class="sign-name">Pig</span><div class="sign-art" role="img" aria-label="Cartoon boy in pig costume"></div></div>
  </section>

  <p class="slogan">Find your inner animal</p>
</main>
</body>
</html>
```